VAN WRAP

I would like to have my logo for my electrical contracting company on my 2018 kestrel haulmar 310 lab short roof. I do like the white front and black back. The business is located st George Utah. web site is www.pylonvoltworks.us and phone number is 5550187246.

```html
<!DOCTYPE html>
<html lang="en">
<head>
<meta charset="UTF-8">
<title>Pylonvolt Works — Van Wrap Side Panel</title>
<link href="https://fonts.googleapis.com/css2?family=Montserrat:wght@700;800&display=swap" rel="stylesheet">
<style>
  :root {
    --wrap-white: #ffffff;
    --wrap-black: #0d0d0d;
    --wrap-charcoal: #2a2a2a;
    --wrap-red: #d0121b;
    --skirt: #1b1b1b;
    --stage: #ffffff;
    --text-light: #f2f2f2;
  }
  * { margin: 0; padding: 0; box-sizing: border-box; }
  html, body {
    width: 1200px; height: 721px; overflow: hidden;
    background: var(--stage);
    font-family: "Montserrat", sans-serif;
  }
  .canvas { position: relative; width: 1200px; height: 721px; overflow: hidden; }
  .wrap-graphics { position: absolute; inset: 0; }
  .rotated {
    position: absolute;
    transform: translate(-50%, -50%) rotate(-41deg);
    white-space: nowrap;
    display: flex; align-items: center;
  }
  .brand { left: 612px; top: 292px; gap: 10px; }
  .brand-mark { width: 24px; height: 24px; background: var(--wrap-red); flex: none; }
  .brand-name {
    font-weight: 800; font-size: 28px; letter-spacing: 1px;
    color: var(--text-light); line-height: 1;
  }
  .phone { left: 798px; top: 252px; gap: 8px; }
  .phone-icon { width: 22px; height: 22px; flex: none; }
  .phone-number {
    font-weight: 700; font-size: 30px; letter-spacing: 1px;
    color: var(--wrap-black); line-height: 1;
  }
  .website {
    left: 855px; top: 280px;
    font-weight: 700; font-size: 17px; letter-spacing: 1.5px;
    color: var(--text-light); line-height: 1;
  }
  .website .accent { color: var(--wrap-red); }
</style>
</head>
<body>
<main class="canvas">
  <svg class="wrap-graphics" width="1200" height="721" viewBox="0 0 1200 721" aria-hidden="true">
    <rect x="40" y="140" width="1120" height="300" rx="24" fill="var(--wrap-white)" stroke="#d9d9d9" stroke-width="2"/>
    <rect x="40" y="410" width="1120" height="80" rx="10" fill="var(--skirt)"/>
    <polygon points="360,420 700,140 870,140 680,315 640,420" fill="var(--wrap-black)"/>
    <polyline points="360,420 700,140" fill="none" stroke="var(--wrap-red)" stroke-width="5"/>
    <polyline points="870,140 680,315 640,420" fill="none" stroke="var(--wrap-red)" stroke-width="5"/>
    <path d="M710,420 L740,350 L975,140 L1136,140 Q1160,140 1160,164 L1160,420 Z" fill="var(--wrap-black)"/>
    <polygon points="710,420 740,350 975,140 1040,140 780,380 772,420" fill="var(--wrap-charcoal)"/>
    <line x1="790" y1="420" x2="1075" y2="140" stroke="var(--wrap-red)" stroke-width="5"/>
    <rect x="330" y="476" width="235" height="4" fill="var(--wrap-red)"/>
    <polygon points="560,486 620,486 660,452 600,452" fill="var(--wrap-white)"/>
    <polygon points="640,486 665,486 700,452 675,452" fill="var(--wrap-charcoal)"/>
    <line x1="690" y1="486" x2="728" y2="452" stroke="var(--wrap-red)" stroke-width="4"/>
  </svg>

  <div class="rotated brand">
    <span class="brand-mark"></span>
    <span class="brand-name">PYLONVOLT WORKS</span>
  </div>

  <div class="rotated phone">
    <svg class="phone-icon" viewBox="0 0 24 24" aria-hidden="true">
      <path fill="#0d0d0d" d="M6.6 10.8a15.1 15.1 0 0 0 6.6 6.6l2.2-2.2a1 1 0 0 1 1-.25 11.4 11.4 0 0 0 3.6.57 1 1 0 0 1 1 1V20a1 1 0 0 1-1 1A17 17 0 0 1 3 4a1 1 0 0 1 1-1h3.5a1 1 0 0 1 1 1c0 1.25.2 2.45.57 3.57a1 1 0 0 1-.25 1z"/>
    </svg>
    <span class="phone-number">5550187246</span>
  </div>

  <div class="rotated website">WWW.PYLON<span class="accent">VOLTWORKS</span>.US</div>
</main>
</body>
</html>
```